Occupational Therapy Clinic Advertisement

Create an advertisement for a magazine. Below I have attached my original ad (Ad 2020.pdf) . I want the ad changed and it should be eye catching. I would like a eye catching graphics added in the ad. It should be a graphic image that applies to education. I am attaching a sample graphic image of that I liked from someone elses ad- it should not be the same- it just is there to show what I like. Please use the same words from my original ad.Dimensions: 3.75in x 10.3 in

Target Market(s)

Parents of School aged children

Requirements
Must have
• Must have eye catching Graphic. Colors should be eye catching for a typed magazine.

```html
<!DOCTYPE html>
<html lang="en">
<head>
<meta charset="utf-8">
<title>Bright Path OT Services</title>
<link href="https://fonts.googleapis.com/css2?family=Carlito:wght@400;700&display=swap" rel="stylesheet">
<style>
:root{
  --blue:#1e7fd0;
  --blue-light:#2aa8ec;
  --yellow:#f8f400;
  --red:#ee1c1c;
  --ink:#2b2b2b;
  --black:#111;
  --magenta:#e63ce6;
  --violet:#6b5ce6;
  --lime:#7cc418;
  --tick:#5cb82e;
  --gold:#c99a12;
  --crimson:#d21f5c;
  --white:#fff;
}
*{margin:0;padding:0;box-sizing:border-box}
html,body{width:1200px;height:3296px;overflow:hidden;background:var(--white)}
body{font-family:"Carlito","Calibri",sans-serif;color:var(--ink);position:relative}
.hero-photo{position:absolute;left:0;top:0;width:1200px;height:1400px;
  background:linear-gradient(180deg,#c9302a 0%,#2f7a3a 22%,#d8d2c8 48%,#f4f2ee 75%,#ffffff 100%)}
.masthead{position:absolute;left:0;top:18px;width:1200px;height:554px;
  background:linear-gradient(90deg,var(--blue) 0%,var(--blue) 55%,var(--blue-light) 100%);
  color:var(--white);text-align:center;font-weight:700}
.masthead .name{font-size:148px;line-height:180px;padding-top:28px;letter-spacing:1px}
.masthead .phone{font-size:98px;line-height:110px;margin-top:0}
.question-band{position:absolute;left:0;top:629px;width:1200px;height:213px;
  background:var(--yellow);color:var(--red);font-weight:700;
  font-size:130px;text-align:center;line-height:213px}
.concerns{position:absolute;left:45px;top:880px;width:1130px;list-style:none;
  font-weight:700;font-size:65px;line-height:86px;color:var(--ink)}
.brick-art{position:absolute;left:220px;top:1345px;width:870px;height:410px;border-radius:30px;
  background:linear-gradient(160deg,#fff36a 0%,#f6dc1a 55%,#e2b80c 100%)}
.promise{position:absolute;left:0;top:1780px;width:1200px;text-align:center;
  font-weight:700;font-size:104px;line-height:128px;color:var(--ink)}
.promise .struck{color:#9a9a9a;position:relative}
.promise .struck svg{position:absolute;left:0;top:18px;width:100%;height:90px}
.approach{position:absolute;left:40px;top:2045px;width:1130px;list-style:none;
  font-size:70px;line-height:84px;color:var(--black)}
.approach li{margin-bottom:0}
.we-1{color:var(--magenta)}.we-2{color:var(--violet)}.we-3{color:var(--lime)}
.credentials{position:absolute;left:42px;top:2592px;font-weight:700;font-size:40px;color:var(--black)}
.tick{position:absolute;left:694px;top:2588px;width:96px;height:90px}
.ages{position:absolute;left:848px;top:2572px;font-weight:700;font-size:74px;color:var(--black)}
.location-band{position:absolute;left:0;top:2658px;width:1200px;height:444px;
  background:linear-gradient(180deg,var(--gold) 0%,#cf6a34 50%,var(--crimson) 100%);
  color:var(--white);font-weight:700}
.location-band .where{position:absolute;left:40px;top:30px;font-size:56px;line-height:74px}
.location-band .contact{position:absolute;left:40px;top:178px;font-size:46px;line-height:74px}
.location-band .email{position:absolute;left:0;top:338px;width:1200px;text-align:center;font-size:70px}
.pin{position:absolute;left:982px;top:140px;width:156px;height:200px}
.signature{position:absolute;left:0;top:3150px;width:1200px;text-align:center;
  font-weight:700;font-size:66px;color:var(--black)}
</style>
</head>
<body>
<div class="hero-photo" role="img" aria-label="Photo of colourful toy building blocks"></div>

<header class="masthead">
  <div class="name">Bright Path<br>OT Services</div>
  <div class="phone">(555) 014-2736</div>
</header>

<div class="question-band">Does your child:</div>

<ul class="concerns">
  <li>- Struggle with Reading/Kriah?</li>
  <li>- Knows the information but fails the test?</li>
  <li>- Has difficulty remembering names and dates?</li>
</ul>

<div class="brick-art" role="img" aria-label="Yellow toy brick with a drawn smile"></div>

<p class="promise">Yes Your Child <span class="struck">can<svg viewBox="0 0 100 90" preserveAspectRatio="none"><path d="M5 85 Q45 50 95 5" stroke="#e8141c" stroke-width="7" fill="none" stroke-linecap="round"/></svg></span> Will<br>Succeed in School!</p>

<ul class="approach">
  <li><span class="we-1">We</span> evaluate using standardized Evaluations</li>
  <li><span class="we-2">We</span> Treat the underlying processing deficits</li>
  <li><span class="we-3">We</span> Treat using Researched based technique</li>
</ul>

<div class="credentials">Board of Ed OT RSA's accepted.</div>
<svg class="tick" viewBox="0 0 96 90" aria-hidden="true">
  <circle cx="44" cy="52" r="36" fill="none" stroke="var(--tick)" stroke-width="6"/>
  <path d="M22 50 L40 72 L90 6" fill="none" stroke="var(--tick)" stroke-width="11" stroke-linecap="round" stroke-linejoin="round"/>
</svg>
<div class="ages">AGES 6-18</div>

<section class="location-band">
  <div class="where">Located in Borough Park. Evaluations done<br>in Borough Park &amp; Staten Island.</div>
  <div class="contact">For more information or to be added to<br>our email list, please email:</div>
  <svg class="pin" viewBox="0 0 156 200" aria-hidden="true">
    <path d="M78 8 C40 8 18 36 18 66 C18 100 50 130 78 170 C106 130 138 100 138 66 C138 36 116 8 78 8 Z" fill="var(--white)"/>
    <circle cx="78" cy="64" r="22" fill="#cf5a3c"/>
    <ellipse cx="78" cy="172" rx="70" ry="20" fill="none" stroke="var(--white)" stroke-width="9"/>
  </svg>
  <div class="email">brightpathot@example.com</div>
</section>

<div class="signature">Dina Halberstam OTR/L (555)014-2736</div>
</body>
</html>
```